依頼詳細
①A6サイズの裏面全面 と A6サイズ表面の下から70mmを使って
デザインをしてください。(両面カラー)

②今回、作成していただきますA6サイズですが、デザインDMとして使用させてもらいますが、クワガタ専門雑誌「MO-RINA」の広告ページ(A4の1面、カラー)として使用させていただきます。
A6サイズ両面のデザインを A4(1面、カラー)になるようにデザインをしてください。

③A6両面の 塗り足しは上下左右3mmずつ 計6mmでお願いします。

④データはイラストレーターCS2で開けるよう保存してください。

記載項目
イベント名:カブトガヤガヤvol.6
テーマ:虫愛 解放!『A BRIGHT HORIZON』
日時:6月13日(土) 12:00~14:00 (開場11:30)
場所:港ステージホール(渋谷)
〒150-0047東京都渋谷区神山町4-18-9 lumora KAMIYA(神山 ルモラ)4階
チケット(前売り):大人2,000円・高校生1,000円・子供(中学生以下)無料
※当日は1,000円分のお食事券代が必要になります
主催:(有)白樺山ファームクワガタ菌床販売部
問い合わせ先TEL:0276-54-3187
※詳しくはホームページでご確認ください。(QRコード有)
出演予定ゲスト:
・フォレストキング藤原氏
・こんちゅう堂岡田氏
・シンガーソングライター 昆虫女子 Miyoさん
・ハッピーダックス(YouTube甲虫ひろば) 北川 浩二氏
イベント内容:
■豪華賞品が当たるじゃんけん大会!
■人気のクワカブを会場で展示販売!
■ヘラクレスとふれあいコーナー!
後援
・(有)フォレストキング
・こんちゅう堂
サイズ
A6
ページ数
両面
希望イメージ
シンプル 複雑
単色 カラフル
暗い 明るい
日常 高級
遊び心 厳粛
未来的 伝統的
女性的 男性的
希望する色
黄・オレンジ系、茶系、無彩色系
納品ファイル
• イラストレーター形式 (.ai)
補足説明
イラストレーターCS2で開けるよう保存してください。

イメージは下記2点でどちらかお好きな方で製作をお願い致します。
➀ギャラクシーロード風
➁アニメ風

```html
<!DOCTYPE html>
<html lang="ja">
<head>
<meta charset="utf-8">
<title>カブトガヤガヤvol.6</title>
<link rel="stylesheet" href="https://fonts.googleapis.com/css2?family=Dela+Gothic+One&family=M+PLUS+Rounded+1c:wght@500;800;900&family=Noto+Sans+JP:wght@700;900&display=swap">
<style>
  :root{
    --space-deep:#03081f;
    --space-mid:#0a2a6e;
    --title-edge:#0b3d9a;
    --sun:#ffd21a;
    --sun-deep:#f5a300;
    --flame:#e8501a;
    --flame-deep:#c2260e;
    --paper:#ffffff;
  }
  *{box-sizing:border-box;margin:0;padding:0}
  html,body{width:850px;height:1200px;overflow:hidden;background:var(--space-deep)}
  .poster{
    position:relative;width:850px;height:1200px;overflow:hidden;
    font-family:"M PLUS Rounded 1c",sans-serif;color:var(--paper);
    background:
      radial-gradient(ellipse 420px 160px at 70% 20%, rgba(120,200,255,.45), transparent 70%),
      radial-gradient(ellipse 600px 300px at 40% 40%, rgba(40,110,210,.55), transparent 70%),
      linear-gradient(160deg, var(--space-mid) 0%, #08195a 35%, var(--space-deep) 70%, #050c2c 100%);
  }
  .streaks{position:absolute;inset:0;width:100%;height:100%}
  .title{
    position:absolute;left:25px;top:40px;width:800px;text-align:center;white-space:nowrap;
    font-family:"Dela Gothic One",sans-serif;font-size:100px;letter-spacing:-2px;
    color:var(--paper);transform:skewX(-8deg);
    -webkit-text-stroke:6px var(--title-edge);paint-order:stroke fill;
    text-shadow:0 0 18px rgba(120,200,255,.8);
  }
  .theme{position:absolute;left:120px;top:190px;transform:skewX(-10deg);white-space:nowrap}
  .theme-jp{
    font-family:"Noto Sans JP",sans-serif;font-weight:900;font-size:40px;line-height:1.2;color:var(--sun);
    text-shadow:0 3px 0 #7a4a00;
  }
  .theme-en{
    font-family:"Noto Sans JP",sans-serif;font-weight:900;font-size:34px;line-height:1.2;letter-spacing:1px;
    color:var(--paper);text-shadow:0 0 10px rgba(120,200,255,.9);
  }
  .vol{
    position:absolute;right:22px;top:172px;white-space:nowrap;
    font-family:"Dela Gothic One",sans-serif;font-size:80px;line-height:1.2;color:var(--sun);
    transform:skewX(-8deg);-webkit-text-stroke:5px #fff;paint-order:stroke fill;
  }
  .beetle-art{
    position:absolute;left:40px;top:300px;width:640px;height:420px;border-radius:45% 55% 40% 50%;
    background:radial-gradient(ellipse at 45% 50%, #d9dde6 0%, #7c8494 35%, #2a3040 65%, rgba(10,20,50,0) 80%);
  }
  .guests-label{
    position:absolute;left:520px;top:618px;width:312px;height:56px;border-radius:28px;
    background:var(--paper);color:var(--title-edge);border:4px solid var(--title-edge);
    font-family:"Noto Sans JP",sans-serif;font-weight:900;font-size:30px;
    display:flex;align-items:center;justify-content:center;gap:10px;
  }
  .guest{position:absolute;width:150px;text-align:center}
  .guest-photo{
    width:136px;height:136px;margin:0 auto;border-radius:50%;border:5px solid var(--paper);
    background:radial-gradient(circle at 50% 40%, #e8c7a8, #8b6a55 60%, #3a3f55);
  }
  .guest-name{margin-top:5px;font-weight:800;font-size:12px;line-height:1.4;color:var(--paper);text-shadow:0 1px 2px #000;white-space:nowrap}
  .guest-name strong{font-size:18px;font-weight:900}
  .events{position:absolute;left:18px;top:730px;width:345px}
  .events-head{
    height:52px;background:var(--paper);border-radius:10px 10px 0 0;
    display:flex;align-items:center;gap:10px;padding-left:16px;
    color:var(--flame);font-family:"Noto Sans JP",sans-serif;font-weight:900;font-size:30px;
  }
  .event-item{
    margin-top:10px;height:96px;border-radius:10px;
    background:linear-gradient(180deg,var(--sun) 0%,var(--sun-deep) 100%);
    border:3px solid var(--paper);padding:9px 14px;white-space:nowrap;
    font-family:"Noto Sans JP",sans-serif;font-weight:900;line-height:1.25;
  }
  .event-item .lead{font-size:25px;color:var(--flame-deep)}
  .event-item .main{font-size:32px;color:var(--paper);-webkit-text-stroke:5px var(--flame-deep);paint-order:stroke fill}
  .info{
    position:absolute;left:18px;top:1108px;width:814px;
    font-weight:800;font-size:12px;line-height:1.45;color:var(--paper);white-space:nowrap;
  }
  .info b{color:var(--sun)}
  .footer{
    position:absolute;left:0;bottom:14px;width:100%;display:flex;justify-content:space-between;padding:0 18px;
    font-weight:800;font-size:15px;color:var(--paper);white-space:nowrap;
  }
</style>
</head>
<body>
<main class="poster">
  <svg class="streaks" viewBox="0 0 850 1200" aria-hidden="true">
    <g stroke="#9fd4ff" stroke-linecap="round" opacity=".35">
      <line x1="0" y1="420" x2="850" y2="120" stroke-width="3"/>
      <line x1="80" y1="560" x2="850" y2="260" stroke-width="2"/>
      <line x1="0" y1="300" x2="700" y2="60" stroke-width="1.5"/>
      <line x1="200" y1="700" x2="850" y2="420" stroke-width="2"/>
    </g>
  </svg>

  <h1 class="title">カブトガヤガヤ</h1>
  <div class="theme">
    <p class="theme-jp">虫愛解放!</p>
    <p class="theme-en">A BRIGHT HORIZON</p>
  </div>
  <p class="vol">vol.6</p>

  <div class="beetle-art" role="img" aria-label="大きなクワガタムシの写真"></div>

  <div class="guests-label">出演予定ゲスト
    <svg width="28" height="28" viewBox="0 0 30 30" aria-hidden="true"><circle cx="15" cy="15" r="13" fill="var(--sun)"/></svg>
  </div>

  <div class="guest" style="left:530px;top:688px">
    <div class="guest-photo" role="img" aria-label="ゲスト北川浩二氏の写真"></div>
    <p class="guest-name">ハッピーダックス<br>(YouTube甲虫ひろば)<br><strong>北川 浩二</strong>氏</p>
  </div>
  <div class="guest" style="left:688px;top:688px">
    <div class="guest-photo" role="img" aria-label="ゲストMiyoさんの写真"></div>
    <p class="guest-name">シンガーソングライター<br>昆虫女子 <strong>Miyo</strong>さん</p>
  </div>
  <div class="guest" style="left:530px;top:905px">
    <div class="guest-photo" role="img" aria-label="ゲスト藤原氏の写真"></div>
    <p class="guest-name">フォレストキング<br><strong>藤原</strong>氏</p>
  </div>
  <div class="guest" style="left:688px;top:905px">
    <div class="guest-photo" role="img" aria-label="ゲスト岡田氏の写真"></div>
    <p class="guest-name">こんちゅう堂<br><strong>岡田</strong>氏</p>
  </div>

  <section class="events">
    <div class="events-head">イベント内容
      <svg width="28" height="28" viewBox="0 0 30 30" aria-hidden="true"><circle cx="15" cy="15" r="13" fill="var(--sun)"/></svg>
    </div>
    <div class="event-item"><p class="lead">豪華賞品が当たる</p><p class="main">じゃんけん大会!</p></div>
    <div class="event-item"><p class="lead">人気のクワガタを</p><p class="main">会場で展示販売!</p></div>
    <div class="event-item"><p class="lead">ヘラクレスと</p><p class="main">ふれあいコーナー!</p></div>
  </section>

  <div class="info">
    <p><b>日時</b> 6月13日(土) 12:00~14:00(開場11:30) <b>場所</b> 港ステージホール(渋谷) 〒150-0047東京都渋谷区神山町4-18-9 lumora KAMIYA(神山 ルモラ)4階</p>
    <p><b>前売り</b> 大人2,000円・高校生1,000円・子供(中学生以下)無料 ※当日は1,000円分のお食事券代が必要 <b>TEL</b> 0276-54-3187</p>
  </div>

  <footer class="footer">
    <span>主催:(有)白樺山ファームクワガタ菌床販売部</span>
    <span>後援・(有)フォレストキング・こんちゅう堂</span>
  </footer>
</main>
</body>
</html>
```